Tesmaro Realty Business Cards

Design business card

Target Market(s)

High-End Buyer of Real Estate over $1 million dollars

Industry/Entity Type

Realtor

Contact Information for Business Card

Lina Tesmaro R(S) LIC.# 41927
Cell 808 555-0163
Email Lina@Tesmaro.net
Website PeakHomeFinds.com

Also Need Cards for:

Glen Tesmaro R(B) LIC# 60418
C 808 555-0192
E Glen@Tesmaro.net
W PeakHomeFinds.com

Colors

Designer to choose colors to be used in the design.

Requirements
Must have
• Address on back:
• 57 Oleander Ct. , Wailea HI 96721
• Logo on back
Nice to have
• I would like the phone numbers and email address to be big so people can read it easily
Should not have
• Very small print Except For: address (57 Oleander Ct. Wailea HI 96721)

```html
<!DOCTYPE html>
<html lang="en">
<head>
<meta charset="utf-8">
<title>Tesmaro Realty Business Cards</title>
<link rel="stylesheet" href="https://fonts.googleapis.com/css2?family=Montserrat:wght@600&family=Questrial&display=swap">
<style>
  :root {
    --backdrop: #5b4a36;
    --card: #000000;
    --silver: #c9c9c9;
    --silver-light: #e6e6e6;
    --white: #ffffff;
    --rule: #8a8a8a;
  }
  html, body {
    margin: 0;
    padding: 0;
    width: 900px;
    height: 1200px;
    overflow: hidden;
    background: var(--backdrop);
  }
  .canvas {
    position: relative;
    width: 900px;
    height: 1200px;
  }
  .card {
    position: absolute;
    left: 82px;
    width: 733px;
    background: var(--card);
    border-radius: 22px;
    overflow: hidden;
  }
  .card-front { top: 138px; height: 427px; }
  .card-back  { top: 633px; height: 429px; }

  .agent-photo {
    position: absolute;
    left: 48px;
    top: 12px;
    width: 390px;
    height: 271px;
    background: radial-gradient(ellipse at 30% 80%, #b8465e 0%, #5a2430 35%, transparent 60%),
                radial-gradient(ellipse at 62% 60%, #3a3a3a 0%, #1a1a1a 45%, transparent 70%),
                #000;
  }
  .front-rule {
    position: absolute;
    left: 48px;
    top: 283px;
    width: 642px;
    height: 1px;
    background: var(--rule);
  }
  .brand-front {
    position: absolute;
    left: 561px;
    top: 45px;
    width: 129px;
    height: 214px;
    display: flex;
    flex-direction: column;
    align-items: center;
    justify-content: center;
    gap: 14px;
  }
  .brand-mark {
    width: 22px;
    height: 22px;
    background: var(--silver);
  }
  .brand-name {
    font-family: "Montserrat", sans-serif;
    font-weight: 600;
    color: var(--silver);
    letter-spacing: 2px;
    text-align: center;
    line-height: 1.3;
  }
  .brand-front .brand-name { font-size: 17px; }

  .agent-name {
    position: absolute;
    left: 48px;
    top: 318px;
    width: 300px;
    text-align: center;
    font-family: "Montserrat", sans-serif;
    font-weight: 600;
    font-size: 22px;
    color: var(--silver);
    letter-spacing: 0.5px;
  }
  .agent-license {
    position: absolute;
    left: 48px;
    top: 352px;
    width: 300px;
    text-align: center;
    font-family: "Questrial", sans-serif;
    font-size: 17px;
    color: var(--silver);
  }
  .contact-list {
    position: absolute;
    right: 42px;
    top: 294px;
    margin: 0;
    padding: 0;
    list-style: none;
    font-family: "Questrial", sans-serif;
    font-size: 26px;
    color: var(--white);
  }
  .contact-item {
    display: flex;
    justify-content: flex-end;
    align-items: center;
    gap: 12px;
    height: 35px;
  }
  .contact-icon { width: 22px; height: 22px; flex: none; }

  .brand-back {
    position: absolute;
    left: 218px;
    top: 127px;
    width: 298px;
    height: 178px;
    display: flex;
    align-items: center;
    justify-content: center;
    gap: 16px;
  }
  .brand-back .brand-mark { width: 30px; height: 30px; }
  .brand-back .brand-name { font-size: 26px; color: var(--silver-light); }

  .office-address {
    position: absolute;
    left: 680px;
    top: 214px;
    width: 0;
    height: 0;
  }
  .office-address span {
    position: absolute;
    left: 0;
    top: 0;
    transform: translate(-50%, -50%) rotate(90deg);
    white-space: nowrap;
    font-family: "Questrial", sans-serif;
    font-size: 11px;
    color: var(--silver);
  }
</style>
</head>
<body>
<div class="canvas">
  <section class="card card-front">
    <div class="agent-photo" role="img" aria-label="Portrait photo of the two agents, a woman in a pink top and a man in a dark suit"></div>
    <div class="brand-front">
      <div class="brand-mark"></div>
      <div class="brand-name">TESMARO<br>REALTY</div>
    </div>
    <div class="front-rule"></div>
    <div class="agent-name">LINA TESMARO R(S)</div>
    <div class="agent-license">LIC.# 41927</div>
    <ul class="contact-list">
      <li class="contact-item">808 555-0163
        <svg class="contact-icon" viewBox="0 0 22 22"><rect x="6" y="1" width="10" height="20" rx="2" fill="none" stroke="#fff" stroke-width="1.6"/><line x1="6" y1="4.5" x2="16" y2="4.5" stroke="#fff" stroke-width="1.2"/><line x1="6" y1="17" x2="16" y2="17" stroke="#fff" stroke-width="1.2"/></svg>
      </li>
      <li class="contact-item">Lina@Tesmaro.net
        <svg class="contact-icon" viewBox="0 0 22 22"><rect x="1" y="5" width="20" height="13" fill="#fff"/><polyline points="1,5 11,13 21,5" fill="none" stroke="#000" stroke-width="1.6"/></svg>
      </li>
      <li class="contact-item">PeakHomeFinds.com
        <svg class="contact-icon" viewBox="0 0 22 22"><circle cx="11" cy="11" r="10" fill="#fff"/><ellipse cx="11" cy="11" rx="4.5" ry="10" fill="none" stroke="#000" stroke-width="1.3"/><line x1="1" y1="11" x2="21" y2="11" stroke="#000" stroke-width="1.3"/><line x1="3" y1="6" x2="19" y2="6" stroke="#000" stroke-width="1.1"/><line x1="3" y1="16" x2="19" y2="16" stroke="#000" stroke-width="1.1"/></svg>
      </li>
    </ul>
  </section>

  <section class="card card-back">
    <div class="brand-back">
      <div class="brand-mark"></div>
      <div class="brand-name">TESMARO<br>REALTY</div>
    </div>
    <div class="office-address"><span>57 Oleander Ct. Wailea HI 96721</span></div>
  </section>
</div>
</body>
</html>
```